ARC VOLLEY Business Card Project

I'd like to request a business card design for the new company I've launched.
The name of the company is "ARC VOLLEY" an indoor unmanned tennis practice facility.
We would like to see designs that use our brand identity color in the logo I've attached.
We hope to get the design with modern, luxurious and elegant tone and manner.
We hope the logo should not be too big.

Business card must have elements as below:
- Logo (One of the logos I've attached)
- Name (In Korean Text) : 박 서 윤
- Title (In Korean Text) : 대표
- Phone Number : 010-8472-3916
- Email Address : seoyun.park@arcvolley-example.co.kr
- Website : www.arcvolley-example.co.kr
- Instagram : arcvolley
- Address (In Korean text) : 경기도 용인시 수지구 풍덕천로 456 미래타워 5층 501호, 502호

Target Market(s)

Tennis amateurs in 20 to 40s

Industry/Entity Type

Sports, Hobby

Contact Information for Business Card

- Logo (One of the logos I've attached) - Name (In Korean Text) : 박 서 윤 - Title (In Korean Text) : 대표 - Phone Number : 010-8472-3916 - Email Address : seoyun.park@arcvolley-example.co.kr - Website : www.arcvolley-example.co.kr - Instagram : arcvolley - Address (In Korean text) : 경기도 용인시 수지구 풍덕천로 456 미래타워 5층 501호, 502호

Font styles to use
Sans Serif

Requirements
Must have
• Double sided
Nice to have
• Logo with intaglio or relief embossing
Should not have
• Logo should not be too big.

```html
<!DOCTYPE html>
<html lang="ko">
<head>
<meta charset="utf-8">
<title>ARC VOLLEY Business Card</title>
<link rel="stylesheet" href="https://fonts.googleapis.com/css2?family=Nanum+Myeongjo&family=Poppins:wght@400;500&display=swap">
<style>
  :root {
    --page: #ffffff;
    --card-green: #2e5239;
    --silver: #d2d2d2;
    --silver-soft: #bfc3c0;
    --divider: #a9b5ac;
  }
  html, body {
    margin: 0;
    padding: 0;
    width: 1200px;
    height: 2319px;
    overflow: hidden;
    background: var(--page);
  }
  .canvas {
    position: relative;
    width: 1200px;
    height: 2319px;
  }
  .card {
    position: absolute;
    left: 125px;
    width: 949px;
    height: 542px;
    background: var(--card-green);
    box-shadow: 0 3px 10px rgba(0,0,0,0.35);
  }
  .card-front { top: 590px; }
  .card-back { top: 1188px; }

  .brand-name {
    position: absolute;
    font-family: "Nanum Myeongjo", serif;
    font-weight: 400;
    color: var(--silver);
    white-space: nowrap;
    letter-spacing: 0.04em;
  }
  .card-front .brand-name {
    left: 0;
    right: 0;
    top: 236px;
    text-align: center;
    font-size: 66px;
    line-height: 70px;
  }
  .card-back .brand-name {
    left: 60px;
    width: 358px;
    top: 249px;
    text-align: center;
    font-size: 40px;
    line-height: 44px;
  }
  .divider {
    position: absolute;
    left: 454px;
    top: 96px;
    width: 1px;
    height: 350px;
    background: var(--divider);
  }
  .person-name {
    position: absolute;
    left: 498px;
    top: 96px;
    margin: 0;
    font-family: "Nanum Myeongjo", serif;
    font-weight: 400;
    font-size: 50px;
    line-height: 58px;
    color: var(--silver-soft);
    letter-spacing: 0.05em;
  }
  .person-title {
    position: absolute;
    left: 500px;
    top: 162px;
    margin: 0;
    font-family: "Nanum Myeongjo", serif;
    font-size: 32px;
    line-height: 38px;
    color: var(--silver);
  }
  .contact-list {
    position: absolute;
    left: 503px;
    top: 232px;
    width: 420px;
    margin: 0;
    padding: 0;
    list-style: none;
    font-family: "Poppins", sans-serif;
    font-weight: 500;
    font-size: 17px;
    line-height: 24px;
    color: var(--silver);
  }
  .contact-list li {
    display: flex;
    align-items: flex-start;
    margin-bottom: 11px;
  }
  .contact-icon {
    width: 16px;
    height: 16px;
    margin: 4px 18px 0 0;
    flex: none;
  }
  .contact-address {
    font-size: 16px;
    line-height: 24px;
    font-weight: 400;
  }
</style>
</head>
<body>
<main class="canvas">
  <section class="card card-front" aria-label="Card front">
    <span class="brand-name">ARC VOLLEY</span>
  </section>

  <section class="card card-back" aria-label="Card back">
    <span class="brand-name">ARC VOLLEY</span>
    <div class="divider"></div>
    <h1 class="person-name">박 서 윤</h1>
    <p class="person-title">대표</p>
    <ul class="contact-list">
      <li>
        <svg class="contact-icon" viewBox="0 0 24 24" aria-hidden="true">
          <path fill="#d2d2d2" d="M6.6 2.5l3 3.2-1.8 2.6c1.3 2.9 3.7 5.3 6.6 6.6l2.6-1.8 3.2 3-1.5 3.6C11 19.5 4.5 13 4.6 3.9z"/>
        </svg>
        <span>010-8472-3916</span>
      </li>
      <li>
        <svg class="contact-icon" viewBox="0 0 24 24" aria-hidden="true">
          <rect x="2" y="5" width="20" height="14" fill="none" stroke="#d2d2d2" stroke-width="2"/>
          <path d="M2 5l10 8 10-8" fill="none" stroke="#d2d2d2" stroke-width="2"/>
        </svg>
        <span>seoyun.park@arcvolley-example.co.kr</span>
      </li>
      <li>
        <svg class="contact-icon" viewBox="0 0 24 24" aria-hidden="true">
          <circle cx="12" cy="12" r="9.5" fill="none" stroke="#d2d2d2" stroke-width="2"/>
          <path d="M2.5 12h19M12 2.5c-3.5 4-3.5 15 0 19M12 2.5c3.5 4 3.5 15 0 19" fill="none" stroke="#d2d2d2" stroke-width="1.6"/>
        </svg>
        <span>www.arcvolley-example.co.kr</span>
      </li>
      <li>
        <svg class="contact-icon" viewBox="0 0 24 24" aria-hidden="true">
          <circle cx="12" cy="12" r="9" fill="none" stroke="#d2d2d2" stroke-width="2"/>
        </svg>
        <span>arcvolley</span>
      </li>
      <li>
        <svg class="contact-icon" viewBox="0 0 24 24" aria-hidden="true">
          <path fill="#d2d2d2" d="M12 2a7 7 0 0 0-7 7c0 5 7 13 7 13s7-8 7-13a7 7 0 0 0-7-7zm0 9.5A2.5 2.5 0 1 1 12 6.5a2.5 2.5 0 0 1 0 5z"/>
        </svg>
        <span class="contact-address">경기도 용인시 수지구 풍덕천로 456<br>미래타워 5층 501호, 502호</span>
      </li>
    </ul>
  </section>
</main>
</body>
</html>
```